Need a business card for our overland brand!

We had the logo made and we need a great design for our business card. Use the logo provide or tweak it however you see fit.

Contact Information for Business Card

Name, Title, Telephone, email, website

```html
<!DOCTYPE html>
<html lang="en">
<head>
<meta charset="utf-8">
<title>Ashford Trails – Business Card</title>
<link rel="stylesheet" href="https://fonts.googleapis.com/css2?family=Poppins:wght@300;400;600;700&display=swap">
<style>
  :root{
    --navy:#253750;
    --teal:#1fa0c6;
    --white:#ffffff;
    --ink:#1a1a1a;
    --rule:#9a9a9a;
    --stage:#e4e6ea;
  }
  *{box-sizing:border-box;margin:0;padding:0}
  html,body{width:1200px;height:1200px;overflow:hidden}
  body{background:var(--stage);font-family:"Poppins",sans-serif;position:relative}
  .card{position:absolute;top:303px;width:370px;height:594px}
  .card--front{left:200px;background:var(--navy)}
  .card--back{left:600px;background:var(--white)}
  .wordmark{position:absolute;left:0;right:0;text-align:center;font-weight:600;
    font-size:48px;line-height:1.2;text-transform:uppercase;letter-spacing:.5px}
  .card--front .wordmark{top:222px;color:var(--white)}
  .card--back .wordmark{top:138px;color:var(--navy)}
  .front-url{position:absolute;left:0;right:0;top:510px;text-align:center;
    color:var(--white);font-weight:300;font-size:16px;letter-spacing:.3px}
  .person{position:absolute;left:0;right:0;top:382px;text-align:center}
  .person__name{color:var(--navy);font-weight:700;font-size:24px;letter-spacing:.6px;line-height:1.1}
  .person__title{color:var(--teal);font-weight:400;font-size:17px;line-height:1.2}
  .icon-row{position:absolute;left:87px;right:87px;top:446px;display:flex;align-items:center;gap:6px}
  .icon-row__rule{flex:1;height:1px;background:var(--rule)}
  .icon-row__rule:first-child{margin-right:2px}
  .icon-row__rule:last-child{margin-left:2px}
  .icon{width:25px;height:25px;background:var(--navy);border-radius:4px;display:flex;align-items:center;justify-content:center}
  .contact{position:absolute;left:0;right:0;top:475px;text-align:center;color:var(--ink);
    font-weight:400;font-size:16px;line-height:21px;letter-spacing:.3px}
</style>
</head>
<body>
  <section class="card card--front">
    <div class="wordmark">Ashford<br>Trails</div>
    <p class="front-url">www.ashfordtrails.com</p>
  </section>

  <section class="card card--back">
    <div class="wordmark">Ashford<br>Trails</div>
    <div class="person">
      <p class="person__name">DANIEL HARPER</p>
      <p class="person__title">Managing Director</p>
    </div>
    <div class="icon-row">
      <span class="icon-row__rule"></span>
      <span class="icon" aria-label="Phone">
        <svg width="16" height="16" viewBox="0 0 16 16"><path d="M2 6c0-2 2.5-3 6-3s6 1 6 3v1h-3V5.5C10 5 9 5 8 5s-2 0-3 .5V7H2z" fill="#fff"/><rect x="4" y="8" width="8" height="6" rx="1" fill="#fff"/><circle cx="8" cy="11" r="1.5" fill="#253750"/></svg>
      </span>
      <span class="icon" aria-label="Email">
        <svg width="16" height="16" viewBox="0 0 16 16"><rect x="1.5" y="3.5" width="13" height="9" fill="none" stroke="#fff" stroke-width="1.2"/><path d="M1.5 3.5 8 9l6.5-5.5M1.5 12.5l5-4.5M14.5 12.5l-5-4.5" fill="none" stroke="#fff" stroke-width="1"/></svg>
      </span>
      <span class="icon" aria-label="Website">
        <svg width="16" height="16" viewBox="0 0 16 16"><circle cx="8" cy="8" r="6.3" fill="#fff"/><ellipse cx="8" cy="8" rx="2.8" ry="6.3" fill="none" stroke="#253750" stroke-width=".9"/><path d="M1.7 8h12.6" stroke="#253750" stroke-width=".9"/></svg>
      </span>
      <span class="icon-row__rule"></span>
    </div>
    <div class="contact">
      <p>044-987 654 321</p>
      <p>hello@ashfordtrails.com</p>
      <p>www.ashfordtrails.com</p>
    </div>
  </section>
</body>
</html>
```